QR Business Card

Design a vertical orientation business card with approved logo and fonts (Jubilee Lines and Aviano). Use metallic gold and black, embossing parts of the logo.
Perhaps color back of card black?
Address:
5873 Harlow Crescent
Level 2
West Palm Beach FL 33455

Delia Porcaro
Managing Partner

Industry/Entity Type

Business

```html
<!DOCTYPE html>
<html lang="en">
<head>
<meta charset="utf-8">
<title>QR – Business Card</title>
<link href="https://fonts.googleapis.com/css2?family=Bodoni+Moda:wght@700&family=Saira:wght@400;500;600&display=swap" rel="stylesheet">
<style>
  :root {
    --backdrop: #8e8e8e;
    --card-white: #ffffff;
    --card-grey: #e4e4e4;
    --ink: #1d1d1d;
    --gold-light: #fbe08a;
    --gold: #e2b33a;
    --gold-deep: #b8862a;
    --text-light: #ffffff;
    --line-light: #bdbdbd;
  }
  * { box-sizing: border-box; margin: 0; padding: 0; }
  html, body { width: 1200px; height: 897px; overflow: hidden; }
  body {
    background: var(--backdrop);
    font-family: "Saira", sans-serif;
    position: relative;
  }
  .card {
    position: absolute;
    top: 108px;
    width: 380px;
    height: 680px;
    border-radius: 6px;
    overflow: hidden;
    box-shadow: 0 10px 30px rgba(0,0,0,.3);
  }
  .card--front { left: 190px; background: var(--card-white); }
  .card--back {
    left: 630px;
    background: linear-gradient(135deg, var(--card-white) 30%, var(--card-grey));
  }
  .card--back::before {
    content: "";
    position: absolute; left: 0; top: 0; bottom: 0;
    width: 12px;
    background: linear-gradient(180deg, var(--gold-light), var(--gold) 40%, var(--gold-deep) 70%, var(--gold-light));
  }
  .card__shape { position: absolute; inset: 0; }

  .brand {
    position: absolute;
    left: 0; right: 0;
    text-align: center;
    color: var(--ink);
  }
  .brand__mark {
    display: block;
    width: 34px; height: 34px;
    margin: 0 auto 12px;
    background: var(--ink);
  }
  .brand__name {
    font-family: "Bodoni Moda", serif;
    font-weight: 700;
    font-size: 26px;
    letter-spacing: 2px;
    text-transform: uppercase;
    line-height: 1;
  }
  .brand__tag {
    font-family: "Bodoni Moda", serif;
    font-weight: 700;
    font-size: 15px;
    letter-spacing: 2px;
    margin-top: 4px;
  }
  .card--front .brand { top: 72px; }
  .card--back .brand { top: 230px; }

  .person {
    position: absolute;
    top: 276px; left: 0; right: 12px;
    text-align: center;
    color: var(--text-light);
  }
  .person__name {
    font-size: 30px; font-weight: 500;
    letter-spacing: 1px; text-transform: uppercase;
    line-height: 1;
  }
  .person__role {
    font-size: 13px; letter-spacing: 1.5px;
    text-transform: uppercase; margin-top: 4px;
  }
  .address {
    position: absolute;
    top: 352px; left: 34px;
    width: 300px; padding: 7px 16px;
    background: linear-gradient(120deg, var(--gold-deep), var(--gold) 35%, var(--gold-light) 55%, var(--gold) 75%, var(--gold-deep));
    border-radius: 10px;
    color: var(--ink);
    font-size: 15px; font-weight: 500;
    line-height: 1.3;
    text-align: center;
  }
  .contacts {
    position: absolute;
    top: 440px; left: 0; right: 12px;
    list-style: none;
    text-align: center;
    color: var(--text-light);
  }
  .contact { margin-bottom: 7px; }
  .contact__icon {
    display: block; margin: 0 auto 3px;
    width: 16px; height: 16px;
  }
  .contact__rule {
    width: 150px; height: 1px;
    margin: 0 auto 3px;
    background: var(--line-light);
  }
  .contact__text { font-size: 14px; letter-spacing: 1px; line-height: 1.4; }

  .web-pill {
    position: absolute;
    left: 30px; right: 18px; bottom: 40px;
    height: 62px;
    background: var(--ink);
    border-radius: 12px;
    color: var(--text-light);
    display: flex; align-items: center; justify-content: center;
    font-size: 18px; letter-spacing: 1px;
  }
</style>
</head>
<body>

<section class="card card--front">
  <svg class="card__shape" viewBox="0 0 380 680" aria-hidden="true">
    <defs>
      <linearGradient id="gold-foil" x1="0" y1="0" x2="1" y2="1">
        <stop offset="0" stop-color="var(--gold-deep)"/>
        <stop offset=".3" stop-color="var(--gold)"/>
        <stop offset=".5" stop-color="var(--gold-light)"/>
        <stop offset=".7" stop-color="var(--gold)"/>
        <stop offset="1" stop-color="var(--gold-deep)"/>
      </linearGradient>
    </defs>
    <path d="M0 262 C 90 188 270 182 380 222 L380 680 L0 680 Z" fill="url(#gold-foil)"/>
    <path d="M0 292 C 90 222 262 216 366 252 L366 680 L0 680 Z" fill="var(--ink)"/>
  </svg>

  <div class="brand">
    <span class="brand__mark"></span>
    <div class="brand__name">QR</div>
    <div class="brand__tag">Design Studio</div>
  </div>

  <div class="person">
    <div class="person__name">Delia Porcaro</div>
    <div class="person__role">Managing Partner</div>
  </div>

  <div class="address">5873 Harlow Crescent, Level 2<br>West Palm Beach<br>FL 33455</div>

  <ul class="contacts">
    <li class="contact">
      <svg class="contact__icon" viewBox="0 0 16 16"><path d="M3 1.5l2.5 0 1 3.5-1.6 1.2a8 8 0 0 0 4.9 4.9L11 9.5l3.5 1v2.5c0 .8-.7 1.5-1.5 1.5A12 12 0 0 1 1.5 3c0-.8.7-1.5 1.5-1.5z" fill="var(--text-light)"/></svg>
      <div class="contact__rule"></div>
      <div class="contact__text">012 555 0148</div>
    </li>
    <li class="contact">
      <svg class="contact__icon" viewBox="0 0 16 16"><rect x="4" y="1" width="8" height="14" rx="1.5" fill="none" stroke="var(--text-light)" stroke-width="1.5"/><circle cx="8" cy="12.5" r=".9" fill="var(--text-light)"/></svg>
      <div class="contact__rule"></div>
      <div class="contact__text">012 555 0149</div>
    </li>
    <li class="contact">
      <svg class="contact__icon" viewBox="0 0 16 16"><rect x="1" y="3" width="14" height="10" rx="1" fill="var(--text-light)"/><path d="M1.5 3.5L8 9l6.5-5.5" fill="none" stroke="var(--ink)" stroke-width="1.2"/></svg>
      <div class="contact__rule"></div>
      <div class="contact__text">delia@qrstudio.com</div>
    </li>
    <li class="contact">
      <svg class="contact__icon" viewBox="0 0 16 16" fill="none" stroke="var(--text-light)" stroke-width="1.2"><circle cx="8" cy="8" r="6.5"/><ellipse cx="8" cy="8" rx="3" ry="6.5"/><path d="M1.5 8h13M2.5 4.5h11M2.5 11.5h11"/></svg>
      <div class="contact__rule"></div>
      <div class="contact__text">www.qrstudio.com</div>
    </li>
  </ul>
</section>

<section class="card card--back">
  <div class="brand">
    <span class="brand__mark"></span>
    <div class="brand__name">QR</div>
    <div class="brand__tag">Design Studio</div>
  </div>
  <div class="web-pill">www.qrstudio.com</div>
</section>

</body>
</html>
```